Kitchen manufaturer business card/logo design

I am a small kitchen manufacturing company that makes and installs all sorts of cabinetry.

The colours im looking to incorporate in the card are light/baby blue, white and black.

Incorporate 5 stars to show quality workmanship and product.

Looking for a modern classy design.
Updates

Hey guys, New idea. The logo should be made using HK in the most modern way possible as well as the full company name below it. Thanks.

Target Market(s)

Anyone with a home thats looking for a new cabinetry of any sort.

Industry/Entity Type

Business

Contact Information for Business Card

Harbor Kitchens
Tod Villaran
PH 0431 582 904
Email- harborkitchens@mailvane.example
ABN- 73 208 561 339
-Kitchens
-Vanities
-Laundries
-Media Units
-Studies
-Wardrobes
-3D Computer Designs

Requirements
Must have

• The front of the card must only have the company name.
The different types of cabinetry I do must be on the back of the card in point form but instead of using points use stars.
Nice to have
• Just think classy and quality

```html
<!DOCTYPE html>
<html lang="en">
<head>
<meta charset="utf-8">
<title>Harbor Kitchens — Business Card</title>
<link rel="stylesheet" href="https://fonts.googleapis.com/css2?family=Tinos&family=Oswald:wght@500&family=Lobster&display=swap">
<style>
  :root {
    --page: #ececec;
    --card-blue: #2bace2;
    --wall-blue: #a9dcf4;
    --panel-blue: #7ccbee;
    --floor-blue: #2bace2;
    --edge: #5fbfe8;
    --ink: #1d2b3a;
    --white: #ffffff;
    --name-blue: #2390c4;
  }
  * { margin: 0; padding: 0; box-sizing: border-box; }
  html, body { width: 1200px; height: 918px; overflow: hidden; background: var(--page); }
  .canvas { position: relative; width: 1200px; height: 918px; }
  .card {
    position: absolute;
    width: 540px;
    height: 310px;
    top: 304px;
    overflow: hidden;
    box-shadow: 0 2px 6px rgba(0,0,0,0.25);
  }
  .card-front { left: 40px; background: var(--card-blue); }
  .card-back { left: 620px; background: var(--wall-blue); }

  .brand {
    position: absolute; left: 0; right: 0; top: 118px;
    text-align: center;
  }
  .brand-name {
    font-family: "Tinos", serif;
    font-size: 24px;
    letter-spacing: 7px;
    color: var(--ink);
  }
  .brand-stars { margin-top: 8px; display: flex; justify-content: center; gap: 4px; }

  .back-shapes { position: absolute; inset: 0; }
  .services {
    position: absolute; left: 30px; top: 36px;
    list-style: none;
    font-family: "Oswald", sans-serif;
    text-transform: uppercase;
    color: var(--ink);
    line-height: 1.25;
  }
  .services li { font-size: 13px; }
  .services li.large { font-size: 17px; margin-top: 6px; }
  .holder {
    position: absolute; left: 270px; top: 42px;
    font-family: "Lobster", cursive;
    font-size: 20px;
    color: var(--name-blue);
  }
  .contact {
    position: absolute; left: 190px; right: 0; top: 128px;
    text-align: center;
    font-family: "Tinos", serif;
    color: var(--ink);
  }
  .contact p { font-size: 19px; line-height: 1.25; }
  .contact p.email { font-size: 16px; }
</style>
</head>
<body>
<div class="canvas">

  <section class="card card-front">
    <div class="brand">
      <div class="brand-name">Harbor Kitchens</div>
      <div class="brand-stars">
        <svg width="100" height="16" viewBox="0 0 100 16" aria-hidden="true">
          <defs>
            <polygon id="star" points="8,0 10,5.5 16,5.8 11.3,9.5 13,15.5 8,12 3,15.5 4.7,9.5 0,5.8 6,5.5" fill="#ffffff"/>
          </defs>
          <use href="#star" x="0"/>
          <use href="#star" x="21"/>
          <use href="#star" x="42"/>
          <use href="#star" x="63"/>
          <use href="#star" x="84"/>
        </svg>
      </div>
    </div>
  </section>

  <section class="card card-back">
    <svg class="back-shapes" width="540" height="310" viewBox="0 0 540 310" aria-hidden="true">
      <polygon points="0,0 185,0 205,215 30,310 0,310" fill="var(--panel-blue)"/>
      <polygon points="205,215 540,290 540,310 30,310" fill="var(--floor-blue)"/>
      <polyline points="185,0 205,215 540,290" fill="none" stroke="var(--edge)" stroke-width="1.5"/>
      <line x1="205" y1="215" x2="30" y2="310" stroke="var(--edge)" stroke-width="1.5"/>
    </svg>
    <ul class="services">
      <li>-Kitchens</li>
      <li>-Vanities</li>
      <li>-Laundries</li>
      <li>-Media Units</li>
      <li class="large">-Studies</li>
      <li class="large">-Wardrobes</li>
      <li class="large">-3D Computer Designs</li>
    </ul>
    <div class="holder">Tod Villaran</div>
    <div class="contact">
      <p>PH: 0431 582 904</p>
      <p class="email">Email: harborkitchens@mailvane.example</p>
      <p>ABN: 73 208 561 339</p>
    </div>
  </section>

</div>
</body>
</html>
```